We need a business card design for a Dubai based company .

We need a business card for a Dubai based company called "Zernova Smoking Requisites Trading LLC". We mainly import Flavoured Tobacco products and Charcoal which is used for smoking in a Hookah/Shisha and distribute to the wholesalers and retailers. Logo file is attached herewith.

```html
<!DOCTYPE html>
<html lang="en">
<head>
<meta charset="utf-8">
<title>Zernova Smoking Requisites Trading LLC – Business Card</title>
<link rel="stylesheet" href="https://fonts.googleapis.com/css2?family=Arimo:wght@400;700&display=swap">
<style>
  :root {
    --stage: #2b2b2e;
    --card-dark: #242426;
    --card-light: #ffffff;
    --brand-red: #c1272d;
    --ink: #1e1e1e;
    --ink-soft: #3a3a3a;
    --white: #ffffff;
    --rule: #555555;
  }
  * { box-sizing: border-box; margin: 0; padding: 0; }
  html, body {
    width: 1200px; height: 654px; overflow: hidden;
    background: var(--stage);
    font-family: "Arimo", Arial, sans-serif;
  }
  .stage {
    width: 1200px; height: 654px;
    display: flex; align-items: center; justify-content: center; gap: 60px;
  }
  .card {
    width: 520px; height: 297px; position: relative;
    box-shadow: 0 10px 28px rgba(0,0,0,.45);
  }
  /* Front */
  .card--front { background: var(--card-light); color: var(--ink); }
  .brand {
    position: absolute; left: 34px; top: 112px;
    display: flex; align-items: center; gap: 12px;
  }
  .brand__mark { width: 14px; height: 14px; background: var(--brand-red); flex: none; }
  .brand__name {
    font-weight: 700; font-size: 15px; line-height: 1.35;
    letter-spacing: .08em; text-transform: uppercase; color: var(--ink);
  }
  .contact { position: absolute; left: 272px; top: 52px; width: 222px; }
  .contact__name { font-weight: 700; font-size: 20px; letter-spacing: .02em; }
  .contact__role { font-size: 14px; color: var(--ink-soft); margin-top: 2px; }
  .contact__rule { border: 0; border-top: 1px solid var(--rule); margin: 10px 0 14px; }
  .contact__list { list-style: none; }
  .contact__item {
    display: flex; gap: 9px; font-size: 10.5px; line-height: 1.45;
    color: var(--ink); margin-bottom: 8px;
  }
  .contact__icon { width: 14px; height: 14px; flex: none; margin-top: 1px; }
  /* Back */
  .card--back {
    background: var(--card-dark); color: var(--white);
    display: flex; flex-direction: column; align-items: center; justify-content: center; gap: 46px;
  }
  .card--back .brand { position: static; }
  .card--back .brand__name { color: var(--white); font-size: 17px; text-align: left; }
  .back__web { font-size: 13px; letter-spacing: .03em; color: var(--white); }
</style>
</head>
<body>
<main class="stage">

  <section class="card card--front" aria-label="Business card front">
    <div class="brand">
      <span class="brand__mark"></span>
      <p class="brand__name">Zernova<br>Smoking Requisites<br>Trading LLC</p>
    </div>

    <div class="contact">
      <h1 class="contact__name">MAREK D</h1>
      <p class="contact__role">CEO</p>
      <hr class="contact__rule">
      <ul class="contact__list">
        <li class="contact__item">
          <svg class="contact__icon" viewBox="0 0 14 14" aria-hidden="true"><circle cx="7" cy="7" r="7" fill="var(--brand-red)"/><path d="M7 3.2a2.4 2.4 0 0 0-2.4 2.4C4.6 7.4 7 10.6 7 10.6s2.4-3.2 2.4-5A2.4 2.4 0 0 0 7 3.2z" fill="#fff"/><circle cx="7" cy="5.6" r=".9" fill="var(--brand-red)"/></svg>
          <span>412 Harbor View Boulevard | Suite 310<br>Bayford | CA | 90512</span>
        </li>
        <li class="contact__item">
          <svg class="contact__icon" viewBox="0 0 14 14" aria-hidden="true"><circle cx="7" cy="7" r="7" fill="var(--brand-red)"/><rect x="3.6" y="4.6" width="6.8" height="4.8" fill="none" stroke="#fff" stroke-width=".9"/><path d="M3.6 4.6 7 7.4l3.4-2.8" fill="none" stroke="#fff" stroke-width=".9"/></svg>
          <span>marekd@zernova.com</span>
        </li>
        <li class="contact__item">
          <svg class="contact__icon" viewBox="0 0 14 14" aria-hidden="true"><circle cx="7" cy="7" r="7" fill="var(--brand-red)"/><path d="M5 3.6c.4 0 .8 1.3.8 1.7 0 .4-.6.6-.6 1 .2.9 1.4 2.1 2.3 2.3.4 0 .6-.6 1-.6.4 0 1.7.4 1.7.8 0 .6-.7 1.5-1.4 1.5-2.4 0-5-2.6-5-5 0-.7.9-1.4 1.5-1.4z" fill="#fff"/></svg>
          <span>Main: 310.555.0142<br>Direct: 310.555.0187<br>Fax: 310.555.0163</span>
        </li>
        <li class="contact__item">
          <svg class="contact__icon" viewBox="0 0 14 14" aria-hidden="true"><circle cx="7" cy="7" r="7" fill="var(--brand-red)"/><circle cx="7" cy="7" r="3.4" fill="none" stroke="#fff" stroke-width=".8"/><ellipse cx="7" cy="7" rx="1.4" ry="3.4" fill="none" stroke="#fff" stroke-width=".8"/><path d="M3.6 7h6.8" stroke="#fff" stroke-width=".8"/></svg>
          <span>www.zernova.com</span>
        </li>
      </ul>
    </div>
  </section>

  <section class="card card--back" aria-label="Business card back">
    <div class="brand">
      <span class="brand__mark"></span>
      <p class="brand__name">Zernova<br>Smoking Requisites<br>Trading LLC</p>
    </div>
    <p class="back__web">www.zernova.com</p>
  </section>

</main>
</body>
</html>
```